Client website

Our designer we were working with had some personal things come up and was unable to finish the design for the site.

We have a .psd file started, and will be attaching it to the project.

Reason: I still want to polish the designs with the current designer and allow more designers the opportunity to participate.

Reason: I'm extending the deadline for another day to give everyone enough time for the final changes our client wants.

I'm trying to extend the deadline so we can get one last set of comps in for my client.  Could everyone message me and let me know how much time they need to do the final tweaks?

Reason: Hey everyone.  I've been sick the last 3 days and I haven't been able to provide feedback on designs.  I'm extending just a few more days so I can catch up here.  Thanks everyone for your patience.

Adults in United States aged 25 to 60 that handle the household budgets and maintenance.

• 1) We need 2 pages. 1 page for flood restoration, 1 page for carpet cleaning

2) The 1-800-# must be the focal point of the website for both pages. People are mostly looking to contact someone ASAP to get them out to their house when flooding occurs.

3) We''re going to have a slide show area to high-light different sub-services offered for each page.

4) We really want a pagenest / lumora feed area. We''re going to use pagenest for special offers, and lumora for weather updates. The pagenest feed is going to be on the carpet cleaning page. The lumora feed is going to be on the flood page.

5) We want an SEO text sections near the bottom.

6) The very bottom will link to the privacy policy and user agreement as well as company name and copyright details.

We really want to stick to the say "theme" that our first designer started with.
• I'm not a designer, so if you think something looks better somewhere, or something can be eliminated, or something can be enhanced, but all means, let us know.

```html
<!DOCTYPE html>
<html lang="en">
<head>
<meta charset="utf-8">
<title>Brightwave – Water &amp; Fire Damage Restoration</title>
<link href="https://fonts.googleapis.com/css2?family=Arimo:wght@400;700&family=PT+Sans:ital,wght@0,400;0,700;1,700&display=swap" rel="stylesheet">
<style>
:root{
  --sand:#d9c6a2;
  --sand-light:#f5efe3;
  --sand-mid:#e6d8bd;
  --brown:#5b4f43;
  --brown-dark:#3f3326;
  --text:#7b6c58;
  --green:#23a023;
  --green-dark:#178a17;
  --blue:#2fa5dc;
  --white:#ffffff;
  --slate:#77746f;
}
*{box-sizing:border-box;margin:0;padding:0}
html,body{width:1108px;height:1200px;overflow:hidden}
body{
  font-family:"Arimo",Arial,sans-serif;
  background:linear-gradient(180deg,var(--sand-light) 0,#f1e9d9 120px,var(--sand-mid) 140px,var(--sand) 320px,var(--sand) 100%);
  position:relative;color:var(--text);
}
.abs{position:absolute}
.brand{left:129px;top:36px;width:220px;text-align:center}
.brand-mark{width:120px;height:120px;border-radius:50%;margin:0 auto 10px;background:var(--green);}
.brand-name{font-family:"PT Sans",sans-serif;font-weight:700;font-size:32px;color:var(--green);letter-spacing:1px;line-height:1}
.brand-tag{font-size:11px;color:var(--blue);letter-spacing:1px;margin-top:6px;text-transform:uppercase}
.spill-art{left:355px;top:108px;width:365px;height:72px;border-radius:30px;background:linear-gradient(90deg,#b8323a 0,#d9c6a2 45%,#8c7b64 80%,#b09a78 100%);opacity:.6}
.call-note{left:790px;top:18px;width:190px;height:170px;background:linear-gradient(160deg,#f3f2e6,#dcdac8);transform:rotate(-18deg);box-shadow:4px 6px 10px rgba(0,0,0,.2)}
.call-text{left:780px;top:70px;width:210px;transform:rotate(-18deg);font-family:"PT Sans",sans-serif;font-style:italic;font-weight:700;text-align:center}
.call-text .num{color:var(--blue);font-size:21px;display:block}
.call-text .cta{color:var(--green);font-size:36px;display:block;line-height:1.1}
.pin{left:836px;top:8px;width:18px;height:18px;border-radius:50%;background:var(--green)}
.nav{left:128px;top:233px;width:854px;height:42px;background:var(--white);border-radius:4px;display:flex;align-items:center;padding-left:22px}
.nav a{font-family:"PT Sans",sans-serif;font-weight:700;font-size:16px;color:var(--green);text-decoration:none;margin-right:36px}
.share{display:flex;align-items:center;gap:6px;height:28px;padding:0 9px;border-radius:3px;color:var(--white);font-size:12px;margin-right:10px}
.share i{width:16px;height:16px;background:var(--white);display:block;opacity:.8}
.share.lumora{background:#8fd3ee;margin-left:2px}
.share.pagenest{background:#4865a8}
.search{margin-left:14px;width:156px;height:28px;border:2px solid #a8dcf2;border-radius:4px;font-size:11px;color:#888;padding:6px 7px}
.search-btn{margin-left:9px;font-family:"PT Sans",sans-serif;font-style:italic;font-weight:700;color:var(--blue);font-size:16px}
.slider{left:128px;top:295px;width:854px;height:300px;border-radius:4px;overflow:hidden;box-shadow:0 10px 14px -6px rgba(60,45,30,.5);display:flex}
.slide-copy{width:306px;background:linear-gradient(180deg,#6f6c68,#8f8b84);color:var(--white);padding:28px 28px 0}
.slide-copy h2{font-family:"PT Sans",sans-serif;font-style:italic;font-weight:700;font-size:27px;margin-bottom:32px}
.slide-copy p{font-size:16px;line-height:22px}
.btn-read{display:inline-block;margin-top:38px;background:#ecebdf;color:var(--green);font-size:12px;padding:7px 16px;border-radius:3px}
.slide-photo{flex:1;background:linear-gradient(120deg,#f2e6d8 0,#d9b691 40%,#e8d9c4 70%,#f0e6d8 100%)}
.dots{left:500px;top:615px;display:flex;gap:13px}
.dots span{width:17px;height:17px;border-radius:50%;background:#e9e5cc;border:1px solid #c4b898}
.dots span.on{background:#968a70}
.article{left:157px;width:490px}
.article h3{font-family:"PT Sans",sans-serif;font-style:italic;font-weight:700;font-size:27px;color:var(--brown-dark);margin-bottom:4px}
.article p{width:318px;font-size:12.5px;line-height:22px}
.article p b{color:var(--green)}
.article .pic{position:absolute;left:336px;top:24px;width:159px;height:129px;border:3px solid #9e8e78;background:linear-gradient(135deg,#ffffff,#7fb8d6 50%,#3d6e96)}
.info{left:751px;top:664px;width:231px;height:304px;background:var(--brown);border-radius:4px;padding:10px 16px;color:#eee6d8}
.info h4{font-family:"PT Sans",sans-serif;font-style:italic;font-weight:700;font-size:27px;margin-bottom:8px;display:flex;justify-content:space-between}
.info h4 i{width:28px;height:28px;background:#e8e0d0;display:block;border-radius:3px;margin-top:4px}
.info p{font-size:12.5px;line-height:22px;letter-spacing:.2px}
.btn-contact{position:absolute;left:13px;top:248px;width:203px;height:41px;background:linear-gradient(180deg,#3bc23b,var(--green-dark));border-radius:3px;color:var(--white);font-family:"PT Sans",sans-serif;font-style:italic;font-weight:700;font-size:26px;text-align:center;line-height:41px}
.vacuum-art{left:738px;top:968px;width:167px;height:120px;border-radius:50%;background:radial-gradient(circle,#a08b62 0,rgba(200,180,140,.3) 60%,transparent 72%)}
.dog-art{left:262px;top:1036px;width:110px;height:110px;border-radius:40%;background:radial-gradient(circle,#4a4a4a 0,#b9a78a 60%,transparent 72%)}
.floor-art{left:160px;top:1116px;width:620px;height:30px;background:radial-gradient(ellipse,rgba(90,80,70,.25),transparent 70%)}
.footer{left:128px;top:1156px;width:854px;height:30px;background:var(--brown);border-radius:3px;color:#e8dfce;font-size:11.5px;display:flex;align-items:center;padding:0 12px}
.footer nav{margin-left:auto;display:flex;gap:30px;padding-right:6px}
.footer a{color:#e8dfce;text-decoration:none}
</style>
</head>
<body>
<div class="abs brand">
  <div class="brand-mark"></div>
  <div class="brand-name">BRIGHTWAVE</div>
  <div class="brand-tag">Water &amp; Fire Damage Restoration</div>
</div>
<div class="abs spill-art" role="img" aria-label="Illustration of a spilled wine glass and coffee cup"></div>
<div class="abs call-note"></div>
<div class="abs pin"></div>
<div class="abs call-text"><span class="num">+0 555 010 2030</span><span class="cta">Call Us</span></div>

<div class="abs nav">
  <a href="#">Home</a><a href="#">About</a><a href="#">Services</a><a href="#">FAQ</a><a href="#">Contact</a>
  <span class="share lumora"><i></i>lumora</span>
  <span class="share pagenest"><i></i>pagenest</span>
  <span class="search">keyword</span>
  <span class="search-btn">Search</span>
</div>

<section class="abs slider">
  <div class="slide-copy">
    <h2>Lorem Ipsum dolor</h2>
    <p>Lorem ipsum dolor sit amet, consectetur adipiscing elit. Aenean blandit tincidunt laoreet. Maecenas lacus sapien, auctor eget rutrum in, tincidunt vitae turpis.</p>
    <span class="btn-read">read more</span>
  </div>
  <div class="slide-photo" role="img" aria-label="Photo of two people relaxing on a clean carpet"></div>
</section>
<div class="abs dots"><span></span><span class="on"></span><span></span><span></span></div>

<article class="abs article" style="top:648px">
  <h3>Lorem Ipsum Dolor</h3>
  <p>Lorem ipsum dolor sit amet, consectetur adipiscing elit. Aenean id eros at eros egestas lacinia vel non arcu. Fusce aliquam justo eu nulla gravida sit amet imperdiet nibh congue. Phasellus interdum lectus vel purus scelerisque et blandit massa tempus. Aenean eu lectus nulla, ac feugiat massa. <b>[Read more]</b></p>
  <div class="pic" role="img" aria-label="Photo of drying fans and dehumidifiers"></div>
</article>
<article class="abs article" style="top:842px">
  <h3>Lorem Ipsum Dolor</h3>
  <p>Lorem ipsum dolor sit amet, consectetur adipiscing elit. Aenean id eros at eros egestas lacinia vel non arcu. Fusce aliquam justo eu nulla gravida sit amet imperdiet nibh congue. Phasellus interdum lectus vel purus scelerisque et blandit massa tempus. Aenean eu lectus nulla, ac feugiat massa. <b>[Read more]</b></p>
  <div class="pic" role="img" aria-label="Photo of drying fans and dehumidifiers"></div>
</article>

<aside class="abs info">
  <h4>Info <i></i></h4>
  <p>Lorem ipsum dolor sit amet, consectetur adipiscing elit. Aenean id eros at eros egestas lacinia vel non arcu. Fusce aliquam justo eu nulla gravida sit amet imperdiet nibh congue. Phasellus interdum lectus vel purus scelerisque et blandit massa tempus.</p>
  <span class="btn-contact">Contact Us</span>
</aside>

<div class="abs vacuum-art" role="img" aria-label="Illustration of a vacuum cleaner on a dusty stain"></div>
<div class="abs floor-art" role="img" aria-label="Illustration of scattered dirt on the floor"></div>
<div class="abs dog-art" role="img" aria-label="Illustration of a puppy beside a food bowl"></div>

<footer class="abs footer">
  <span>BRIGHTWAVE &nbsp;© 2011 | PRIVACY POLICY</span>
  <nav><a href="#">Home</a><a href="#">About</a><a href="#">Services</a><a href="#">FAQ</a><a href="#">Contact</a></nav>
</footer>
</body>
</html>
```